Need 8.5" x 11" as well as large 11"x17" Posters for our upcoming event

Please include LOGOs in poster
Main logo is Harborview Teen Circle of PL

All high school age faith groups are invited to come and join with 150 to 175 other high school students from various faith traditions to participate in the Harborview Teen Circle of Pine Lakes‘s Annual Kindred Voices Gathering. More than ever, our county and world need young leaders who are willing to learn from each other and build stronger communities!

KINDRED GATHERING
The purpose of this Interfaith Youth Forum is to bring together young people from diverse ethnic, cultural, and religious backgrounds, and to engage them in dialogue. True dialogue is a conversation on a common subject between two or more persons of differing points of view and/or backgrounds. We feel that this commitment to dialogue will affect relationships in a constructive way in our places of worship and in our community.
The forum itself involves having eight religiously diverse high school-age students, one adult, and youth leader around each table to discuss common questions. Our youth leaders act as facilitators, but it is stressed that it is the students we want to hear from.
RSVP for our KINDRED GATHERING before February 18th, 2018
FORUM QUESTIONS Available online at http://htcpl-example.org/home/kindred-fair/

Target Market(s)

Houses of worship, community leaders, High School Students

Industry/Entity Type

Non-Profit

Font styles to use
Serif

Colors
cfdeed
0255a3
f78f20
f37122
f68d4d
faa54b
ffcf3e
ffc214
34a6d7

Requirements
Must have
• Harborview Teen Circle of Pine Lakes's 14th Annual Kindred Gathering & Fair
• TEENS EXPRESSING THEIR FAITH THROUGH ART, MUSIC, AND DIALOGUE
• THIS YEAR'S THEME: “Who Are You?”
• Sunday, March 11th, 2018 11:00am-5:00pm
• Congregation Ner Adamah
• 4187 W Larkmont Rd. Santa Ana, CA 92705
• Email: htcplorg@mailbox-example.com
• Website: HTCPL-example.org
• Facebook: Harborview Teen Circle of Pine Lakes
Nice to have
• Descriptions provided in word doc
Should not have
• -

```html
<!DOCTYPE html>
<html lang="en">
<head>
<meta charset="utf-8">
<title>Harborview Teen Circle of Pine Lakes — 14th Annual Kindred Gathering &amp; Fair</title>
<link rel="stylesheet" href="https://fonts.googleapis.com/css2?family=Oswald:wght@600&family=Arimo&family=Tinos&family=Open+Sans:wght@400&display=swap">
<style>
  :root {
    --stage: #8c8c8c;
    --blue: #0255a3;
    --blue-deep: #0a3d86;
    --yellow: #ffcf3e;
    --white: #ffffff;
    --ink: #1a1a1a;
    --photo-red: #9b1c28;
    --photo-blue: #3a78b8;
  }
  * { margin: 0; padding: 0; box-sizing: border-box; }
  html, body { width: 1200px; height: 1200px; overflow: hidden; }
  body { background: var(--stage); position: relative; }

  .poster {
    position: absolute; left: 133px; top: 0;
    width: 933px; height: 1200px; overflow: hidden;
    color: var(--white);
  }
  .poster-shapes { position: absolute; inset: 0; }

  .title {
    position: absolute; left: 0; right: 0; top: 518px;
    text-align: center;
    font-family: "Oswald", "Arial Narrow", sans-serif; font-weight: 600;
    font-size: 45px; line-height: 55px; letter-spacing: -0.3px;
  }
  .title-rule {
    position: absolute; left: 230px; width: 491px; top: 636px;
    height: 2px; background: rgba(255,255,255,0.85);
  }
  .tagline, .theme {
    position: absolute; left: 0; right: 0; text-align: center;
    font-family: "Arimo", Arial, sans-serif; font-size: 22.5px;
  }
  .tagline { top: 656px; }
  .theme { top: 702px; font-size: 22px; }
  .when, .where {
    position: absolute; left: 0; right: 0; text-align: center;
    font-family: "Tinos", "Times New Roman", serif; font-size: 25px;
    letter-spacing: 0.6px;
  }
  .when { top: 749px; }
  .where { top: 794px; }
  .where .sep { margin: 0 10px; }
  .invite {
    position: absolute; left: 30px; width: 880px; top: 852px;
    font-family: "Open Sans", Arial, sans-serif; font-size: 14.6px; line-height: 21.5px;
  }

  .contacts { position: absolute; left: 322px; top: 1030px; list-style: none; }
  .contacts li {
    display: flex; align-items: center; height: 45px;
    font-family: "Arimo", Arial, sans-serif; font-size: 17px; color: var(--ink);
  }
  .contacts svg { width: 28px; height: 28px; margin-right: 14px; flex: none; }
  .contacts .square { width: 28px; height: 28px; background: var(--blue); margin-right: 14px; flex: none; }

  .divider { position: absolute; left: 706px; top: 1010px; width: 2px; height: 144px; background: var(--ink); }

  .client-mark {
    position: absolute; left: 738px; top: 1015px; width: 144px; height: 144px;
    border: 3px solid var(--ink); border-radius: 50%;
    display: flex; align-items: center; justify-content: center; text-align: center;
    font-family: "Arimo", Arial, sans-serif; font-size: 14px; line-height: 17px; color: var(--ink);
  }

  .partner {
    position: absolute; top: 1142px;
    font-family: "Tinos", "Times New Roman", serif; color: var(--blue);
  }
  .partner-one { left: 24px; font-size: 17px; line-height: 17px; width: 100px; }
  .partner-two { left: 140px; top: 1155px; font-size: 13px; width: 140px; }
</style>
</head>
<body>
<main class="poster">
  <svg class="poster-shapes" viewBox="0 0 933 1200" width="933" height="1200">
    <defs>
      <radialGradient id="blueField" cx="50%" cy="55%" r="70%">
        <stop offset="0" stop-color="#0e5fb0"/>
        <stop offset="1" stop-color="#0a3d86"/>
      </radialGradient>
      <linearGradient id="groupPhoto" x1="0" y1="0" x2="0" y2="1">
        <stop offset="0" stop-color="#9b1c28"/>
        <stop offset="0.35" stop-color="#7a2030"/>
        <stop offset="0.7" stop-color="#3a78b8"/>
        <stop offset="1" stop-color="#6b6058"/>
      </linearGradient>
      <linearGradient id="singerPhoto" x1="0" y1="0" x2="1" y2="1">
        <stop offset="0" stop-color="#c9b8a6"/>
        <stop offset="1" stop-color="#5c5550"/>
      </linearGradient>
      <linearGradient id="drummerPhoto" x1="0" y1="0" x2="1" y2="1">
        <stop offset="0" stop-color="#efe6e2"/>
        <stop offset="1" stop-color="#7a5a42"/>
      </linearGradient>
    </defs>

    <rect class="field" width="933" height="1200" fill="url(#blueField)"/>

    <path class="accent-top" fill="var(--yellow)"
      d="M0,205 C80,380 250,490 420,487 C600,485 760,400 933,300 V322 C770,425 600,508 420,510 C230,512 60,430 0,300 Z"/>
    <path class="group-photo" role="img" aria-label="Group photo of teen participants standing in front of a red stage curtain"
      fill="url(#groupPhoto)"
      d="M0,0 H933 V300 C760,400 600,485 420,487 C250,490 80,380 0,205 Z"/>

    <circle cx="755" cy="396" r="118" fill="var(--yellow)"/>
    <circle cx="755" cy="396" r="111" fill="var(--white)"/>
    <circle class="singer-photo" role="img" aria-label="Photo of teens performing music at a microphone"
      cx="755" cy="396" r="107" fill="url(#singerPhoto)"/>

    <path class="accent-bottom" fill="var(--yellow)"
      d="M180,1012 C420,965 700,955 933,1010 V1040 C700,990 420,1000 180,1040 Z"/>
    <path class="footer-field" fill="var(--white)"
      d="M0,1075 C250,1015 620,985 933,1040 V1200 H0 Z"/>

    <circle cx="110" cy="1025" r="95" fill="var(--yellow)"/>
    <circle cx="110" cy="1025" r="89" fill="var(--white)"/>
    <circle class="drummer-photo" role="img" aria-label="Photo of a teen playing drums"
      cx="110" cy="1025" r="85" fill="url(#drummerPhoto)"/>
  </svg>

  <h1 class="title">Harborview Teen Circle of Pine Lakes's 14th<br>Annual Kindred Gathering &amp; Fair</h1>
  <div class="title-rule"></div>
  <p class="tagline">TEENS EXPRESSING THEIR FAITH THROUGH ART, MUSIC, AND DIALOGUE</p>
  <p class="theme">INTERFAITH YOUTH FORUM THIS YEAR'S THEME: “Who Are You?”</p>
  <p class="when">Sunday, March 11th, 2018 11:00am-5:00pm</p>
  <p class="where">Congregation Ner Adamah <span class="sep">|</span> 4187 W Larkmont Rd. Santa Ana <span class="sep">|</span> CA 92705</p>
  <p class="invite">All high school age faith groups are invited to come and join with 150 to 175 other high school students from various faith traditions to participate in the Harborview Teen Circle of Pine Lakes‘s Annual Kindred Voices Gathering. More than ever, our county and world need young leaders who are willing to learn from each other and build stronger communities!</p>

  <ul class="contacts">
    <li>
      <svg viewBox="0 0 28 28" aria-hidden="true"><rect x="2" y="6" width="24" height="16" fill="none" stroke="#1a1a1a" stroke-width="2.5"/><path d="M2,6 L14,16 L26,6" fill="none" stroke="#1a1a1a" stroke-width="2.5"/></svg>
      htcplorg@mailbox-example.com
    </li>
    <li>
      <svg viewBox="0 0 28 28" aria-hidden="true"><circle cx="14" cy="14" r="12" fill="none" stroke="#1a1a1a" stroke-width="2.5"/><ellipse cx="14" cy="14" rx="5" ry="12" fill="none" stroke="#1a1a1a" stroke-width="2"/><path d="M2,14 H26" stroke="#1a1a1a" stroke-width="2"/></svg>
      HTCPL-example.org
    </li>
    <li><span class="square"></span>Harborview Teen Circle of Pine Lakes</li>
  </ul>

  <div class="divider"></div>
  <div class="client-mark">Harborview<br>Teen Circle<br>of Pine Lakes</div>

  <div class="partner partner-one">Brightpath Allies</div>
  <div class="partner partner-two">Congregation Ner Adamah</div>
</main>
</body>
</html>
```